Internationally renowned speaker/campaigner needs a book cover

I need a preliminary cover design for my new book "HALF-LIGHT".

I'm a medical doctor and an internationally renowned speaker and campaigner for human-centered and compassionate healthcare, co-founder of an international social movement KINDLING in CLINICS (http://kindlinginclinics.example), and successful author of the book 'PAUSE AND LISTEN - Ways to cherish your practice and your people' (http://www.bookvaultstore.example/PAUSE-LISTEN-cherish-your-practice/dp/9082614530)

The subtitle of HALF-LIGHT is: "How our half-sighted mechanistic thinking leads to division, scarcity, conflict, burnout, sickness and a damaged living planet (and how we can turn it around)"

Author: Dr GARETH PELLIMORE

Preliminary book blurb:
"As social activists and environmental campaigners we are continuously sabotaging our cause because our strategies are unconsciously supporting the materialistic foundations of our broken world.

Our materialistic science sees the natural world and even people as innate objects, without consciousness or connection. Modern medicine treats patients as broken machines to be fixed, not as conscious, subjective beings. And economic theory says every person is an independent agent, striving to maximize advantage. We turn every human and natural gift into a commodity to be owned, controlled, bought and sold.

Our social policies, education system, justice system and even our democracy assume that incentives, rewards and punishments are the ‘real’ motives for human behavior. Our purpose in life is to ‘get ahead’ and accumulate material goods. Therein lies competition, insecurity, greed, violence, ill-health and the destruction of the natural environment.

Materialistic science is simply blind to the life-world of consciousness, intelligence, purpose and deep interdependence in all natural and human systems. We all know that compassion, kindness, love, and human creativity are the real foundation of our communities, not mindless competition.

But so immersed are we in materialistic assumptions, that in our campaigns we mistakenly adopt tools and strategies from the existing system in our struggle for a better world. But the moment we fight against anything, or demonize our opposition, or sell our ideas for money, or charitably impose our solutions, we only strengthen the material world.

Instead, we have to be the change we want to see: grow an economy of generosity and gifting, freely share ideas, focus on solutions not problems, and deeply believe in the capacity for creativity and healing in every person and every community. You can download this book for free at halflightbook.org."

Design brief
I need a compelling front page image and title design that conveys the idea that our science is one-eyed or half-blind, hence the title name 'half-light', which means half-science.

Our predominant science only sees the material world, not the conscious world. We need both.

I'm also preparing a IDEAx talk on the subject and want the compelling image and title to use for this purpose also.

The genre of books is in the class of leadership, entrepreneurs, positive psychology, community development - and I have uploaded some cover images of books in this class. The cover of my current book, PAUSE AND LISTEN, has elements of the style I'm looking for: bold, bright, simple, metaphorical, a surprising juxtaposition of technical and human.

The way I develop and market the book will be congruent with the ideas expressed. I will give the e-book away for free and invite people to make a donation if they like it (gift economy). The book will be published on the website unfinished, inviting comments, suggestions, stories and ideas to be included in the finished book. So to a degree, the content of the book will be fully developed by crowdsourcing living examples of the core ideas and creating a community of conversation (including a Chatterly page). I'll later be looking for a simple WordPress website design based on the book cover graphic, fonts and colours.

So this first design brief and contract is for an e-book cover and later the book will be self-published as a paperback using PressNest.

Target Market(s)

The target audience is readers who are community leaders and social activists - all those utterly passionate about creating a better world, whether it's in the environment, education, healthcare, violence prevention, justice, health communities, etc.

Font styles to use
Sans Serif

Requirements
Must have
• A compelling image that symbolises the key idea - eyecatching
Should not have
• Must not express 'corporate' concepts, power or hierarchy

```html
<!DOCTYPE html>
<html lang="en">
<head>
<meta charset="utf-8">
<title>HALF-LIGHT — Book Cover</title>
<link rel="stylesheet" href="https://fonts.googleapis.com/css2?family=League+Gothic&family=Oswald:wght@300;500&display=swap">
<style>
  :root {
    --paper: #ffffff;
    --title-pink: #dc1a5e;
    --subtitle-grey: #55575c;
    --band-red: #a3110f;
    --author-white: #ffffff;
    --brain-grey: #b9b9b9;
    --brain-dark: #6f6f6f;
    --splash-blue: #aee0f0;
    --splash-yellow: #fbeeb0;
    --splash-pink: #f4b6c8;
  }
  html, body {
    margin: 0;
    padding: 0;
    overflow: hidden;
    background: var(--paper);
  }
  .cover {
    position: relative;
    width: 750px;
    height: 1200px;
    background: var(--paper);
    overflow: hidden;
  }
  .cover svg { position: absolute; left: 0; top: 0; }
  .title {
    font-family: "League Gothic", "Oswald", sans-serif;
    fill: var(--title-pink);
  }
  .subtitle {
    font-family: "League Gothic", "Oswald", sans-serif;
    fill: var(--subtitle-grey);
  }
  .subtitle .accent {
    fill: var(--title-pink);
    font-family: "Oswald", sans-serif;
    font-weight: 300;
    font-style: italic;
  }
  .tagline {
    font-family: "Oswald", sans-serif;
    font-weight: 300;
    fill: var(--title-pink);
  }
  .author-band { fill: var(--band-red); }
  .author {
    font-family: "League Gothic", "Oswald", sans-serif;
    fill: var(--author-white);
  }
</style>
</head>
<body>
<main class="cover">
  <svg width="750" height="1200" viewBox="0 0 750 1200" xmlns="http://www.w3.org/2000/svg">
    <defs>
      <linearGradient id="brainTones" x1="0" y1="0" x2="1" y2="0">
        <stop offset="0" stop-color="var(--brain-dark)" stop-opacity="0.35"/>
        <stop offset="0.45" stop-color="var(--brain-grey)"/>
        <stop offset="0.55" stop-color="var(--splash-blue)"/>
        <stop offset="0.78" stop-color="var(--splash-yellow)"/>
        <stop offset="1" stop-color="var(--splash-pink)" stop-opacity="0.5"/>
      </linearGradient>
    </defs>

    <text class="title" x="37" y="230" font-size="246" textLength="675" lengthAdjust="spacingAndGlyphs">HALF-LIGHT</text>

    <g class="subtitle" font-size="38">
      <text x="88" y="292" textLength="574" lengthAdjust="spacingAndGlyphs">How our <tspan class="accent" font-size="33">half-sighted mechanistic thinking</tspan> leads to</text>
      <text x="70" y="332" textLength="612" lengthAdjust="spacingAndGlyphs">DIVISION, SCARCITY, CONFLICT, BURNOUT, SICKNESS</text>
      <text x="166" y="370" textLength="418" lengthAdjust="spacingAndGlyphs">AND A DAMAGED LIVING PLANET</text>
    </g>

    <rect class="cover-illustration" x="128" y="424" width="552" height="464" rx="40"
          fill="url(#brainTones)" role="img"
          aria-label="A brain split in two: the left half grey and wired with circuit lines, the right half in soft paint-splash colours"/>

    <text class="tagline" x="146" y="974" font-size="48" textLength="436" lengthAdjust="spacingAndGlyphs">and how we can turn it around</text>

    <rect class="author-band" x="0" y="1069" width="750" height="131"/>
    <text class="author" x="120" y="1182" font-size="128" textLength="512" lengthAdjust="spacingAndGlyphs">Dr GARETH PELLIMORE</text>
  </svg>
</main>
</body>
</html>
```